" Plataforma digital que empresas podem usar para dar acesso a seus funcionarios a benefícios relacionados com cuidado e educação de crianças ate 5 anos: desde dicas praticas, sugestão de produtos, referencias de prestadores de serviços ate produtos financeiros - tudo relacionado com esta etapa da vida. "

```html
<!DOCTYPE html>
<html lang="pt-BR">
<head>
<meta charset="utf-8">
<title>Sorri — Envelope</title>
<link rel="stylesheet" href="https://fonts.googleapis.com/css2?family=Baloo+2:wght@700&family=Nunito:wght@600&display=swap">
<style>
  :root {
    --orange: #f36b12;
    --orange-deep: #e35f0a;
    --orange-soft: #f58a3c;
    --paper: #ffffff;
    --backdrop: #d9dadb;
    --ink: #5a5a5a;
  }
  * { margin: 0; padding: 0; box-sizing: border-box; }
  html, body { width: 1200px; height: 1200px; overflow: hidden; }
  body {
    background: var(--backdrop);
    position: relative;
    font-family: "Nunito", sans-serif;
  }
  .envelope {
    position: absolute;
    top: 230px;
    width: 470px;
    height: 680px;
    overflow: hidden;
  }
  .envelope--front { left: 95px; background: var(--paper); }
  .envelope--back { left: 635px; background: var(--orange); }

  .envelope__flap {
    position: absolute;
    top: 0; left: 0;
    width: 100%; height: 34px;
    z-index: 2;
  }

  .brand-area {
    position: absolute;
    border-radius: 50%;
  }
  .envelope--front .brand-area {
    left: 110px;
    top: 250px;
    width: 440px;
    height: 440px;
    background: radial-gradient(circle at 45% 45%, var(--orange) 0%, var(--orange-soft) 55%, rgba(243,107,18,0.15) 100%);
  }
  .envelope--back .brand-area {
    left: 150px;
    top: 250px;
    width: 480px;
    height: 480px;
    background: var(--orange-deep);
  }

  .brand-name {
    font-family: "Baloo 2", sans-serif;
    font-weight: 700;
    letter-spacing: 1px;
    line-height: 1;
    position: absolute;
    left: 0; right: 0;
    text-align: center;
    z-index: 1;
  }
  .envelope--front .brand-name {
    top: 88px;
    font-size: 52px;
    color: var(--orange);
  }
  .envelope--back .brand-name {
    top: 300px;
    font-size: 72px;
    color: var(--paper);
  }

  .contact-list {
    position: absolute;
    left: 12px;
    bottom: 190px;
    list-style: none;
    display: flex;
    flex-direction: row;
    gap: 3px;
    writing-mode: vertical-rl;
    transform: rotate(180deg);
    z-index: 1;
  }
  .contact-list__item {
    display: flex;
    align-items: center;
    gap: 5px;
    font-size: 8px;
    line-height: 10px;
    color: var(--ink);
    white-space: nowrap;
  }
  .contact-list__icon {
    width: 9px; height: 9px;
    background: var(--orange);
    border-radius: 2px;
    flex: none;
  }
</style>
</head>
<body>
  <section class="envelope envelope--front" aria-label="Frente do envelope">
    <svg class="envelope__flap" viewBox="0 0 470 34" preserveAspectRatio="none" aria-hidden="true">
      <polygon points="0,0 470,0 470,34 440,12 30,12 0,34" fill="var(--orange)"/>
    </svg>
    <div class="brand-name">Sorri</div>
    <div class="brand-area" role="img" aria-label="Grande símbolo sorridente da marca em laranja"></div>
    <ul class="contact-list">
      <li class="contact-list__item"><span class="contact-list__icon"></span>(11) 3000-4000</li>
      <li class="contact-list__item"><span class="contact-list__icon"></span>ola@sorri.app</li>
      <li class="contact-list__item"><span class="contact-list__icon"></span>www.sorri.app</li>
      <li class="contact-list__item"><span class="contact-list__icon"></span>Rua das Palmeiras, 120</li>
      <li class="contact-list__item"><span class="contact-list__icon"></span>São Paulo, SP</li>
    </ul>
  </section>

  <section class="envelope envelope--back" aria-label="Verso do envelope">
    <div class="brand-area" role="img" aria-label="Símbolo sorridente da marca em tom laranja escuro, suave"></div>
    <div class="brand-name">Sorri</div>
  </section>
</body>
</html>
```